Whitcombe Framing Works - Card Design

I am looking to use the logo designs that you already did for me to develop a business card. I would like the card to have a black background and be double sided. I want white and green logo and text. I have attached an inspiration photo of a look that I like. I would like to use the Vertical Logo attached to take up the full front side of the card. On the back where I have my name and information, I would like to have the horizontal logo or maybe even just the image of the 'A' and trees without the text. I am open, but I am looking for something clean and simple and I want the green to really pop! Additional files can be found under Design #: 40593216

Target Market(s)

Homeowners

Industry/Entity Type

Construction

Contact Information for Business Card

Name: Marcus Pellow, Title: Project Manager, Phone: 831.555.0147, Email: whitcombeframingworks@mailbarn.net, address: 418 Juniper Ln, Felton, CA 95092, Lic# 2046318

Colors
00AB8E
00BBA5
67D7C9
C6EFE9
E9F9F6

Requirements
Nice to have
• I would like to see the logos that I have already got from SketchHarbor, though I am open to new ones

```html
<!DOCTYPE html>
<html lang="en">
<head>
<meta charset="utf-8">
<title>Whitcombe Framing Works – Business Card</title>
<link rel="stylesheet" href="https://fonts.googleapis.com/css2?family=Montserrat:wght@400;500;600&display=swap">
<style>
  :root {
    --backdrop: #b3b3b3;
    --card: #000000;
    --ink: #ffffff;
    --green: #6ab547;
  }
  * { margin: 0; padding: 0; box-sizing: border-box; }
  html, body {
    width: 1000px; height: 1200px; overflow: hidden;
    background: var(--backdrop);
    font-family: "Montserrat", sans-serif;
    color: var(--ink);
  }
  .card {
    position: absolute;
    left: 51px; width: 898px; height: 539px;
    background: var(--card);
  }
  .card--info { top: 44px; }
  .card--brand { top: 617px; }

  .brand-lockup {
    position: absolute;
    display: flex; align-items: center; gap: 14px;
    font-weight: 600; color: var(--ink); white-space: nowrap;
  }
  .brand-lockup .brand-mark {
    width: 22px; height: 22px; background: var(--green); flex: none;
  }
  .card--info .brand-lockup {
    left: 450px; top: 138px; width: 390px; justify-content: center;
    font-size: 28px;
  }
  .card--brand .brand-lockup {
    left: 0; right: 0; top: 250px; justify-content: center;
    font-size: 40px;
  }
  .card--brand .brand-lockup .brand-mark { width: 32px; height: 32px; }

  .contact {
    position: absolute; left: 72px; top: 282px;
  }
  .contact__name { font-size: 23px; font-weight: 500; line-height: 1.2; }
  .contact__title { font-size: 20px; font-weight: 400; margin-top: 4px; }
  .contact__list { list-style: none; margin-top: 14px; }
  .contact__item {
    display: flex; align-items: flex-start; gap: 12px;
    font-size: 20px; font-weight: 400; line-height: 33px;
    margin-bottom: 7px;
  }
  .contact__icon { width: 19px; height: 33px; flex: none; }
  .contact__lines span { display: block; }
</style>
</head>
<body>
  <section class="card card--info">
    <div class="brand-lockup"><span class="brand-mark"></span>Whitcombe Framing Works</div>

    <div class="contact">
      <div class="contact__name">Marcus Pellow</div>
      <div class="contact__title">Project Manager</div>
      <ul class="contact__list">
        <li class="contact__item">
          <svg class="contact__icon" viewBox="0 0 19 33" aria-hidden="true">
            <path d="M5 9 L8 8 L10 13 L8 14.5 Q9.5 18 12 20 L13.5 18.5 L17 21 L16 24 Q9 24 5 9 Z" fill="none" stroke="#fff" stroke-width="1.4" stroke-linejoin="round"/>
          </svg>
          <span>831.555.0147</span>
        </li>
        <li class="contact__item">
          <svg class="contact__icon" viewBox="0 0 19 33" aria-hidden="true">
            <rect x="1" y="11" width="17" height="12" fill="none" stroke="#fff" stroke-width="1.4"/>
            <path d="M1 11 L9.5 18 L18 11 M1 23 L7 16.5 M18 23 L12 16.5" fill="none" stroke="#fff" stroke-width="1.4"/>
          </svg>
          <span>whitcombeframingworks@mailbarn.net</span>
        </li>
        <li class="contact__item">
          <svg class="contact__icon" viewBox="0 0 19 33" aria-hidden="true">
            <path d="M9.5 22 Q4 15 4 11.5 A5.5 5.5 0 0 1 15 11.5 Q15 15 9.5 22 Z" fill="none" stroke="#fff" stroke-width="1.4"/>
            <circle cx="9.5" cy="11.5" r="2" fill="none" stroke="#fff" stroke-width="1.3"/>
            <line x1="5" y1="25" x2="14" y2="25" stroke="#fff" stroke-width="1.4"/>
          </svg>
          <span class="contact__lines">
            <span>418 Juniper Ln, Felton, CA 95092</span>
            <span>Lic# 2046318</span>
          </span>
        </li>
      </ul>
    </div>
  </section>

  <section class="card card--brand">
    <div class="brand-lockup"><span class="brand-mark"></span>Whitcombe Framing Works</div>
  </section>
</body>
</html>
```